Food Hall in San Clemente, CA by the Pacific Ocean that has 15 vendors and 2 bars

We need a web page design that highlights our food hall in San Clemente, CA. The name of the food hall is Tidewell Food Hall. Inside of the food hall there are 15 different vendors and 2 bars. The place has a beautiful patio and it is by Pacific Ocean. Most of the vendors are local to San Clemente area. The highly anticipated location is opening during the summer of 2025. Website should have a dropdown menu for the different vendors that are in the food hall and people should be able to click to their respective business website. The website should also include link to our social media channels and also a link to provide comments and subscribe for the mailing list.
Target Market(s)
Mostly residents in the San Clemente, CA and surrounding areas. Couples, families and tourist alike that are looking for an exceptional dining experience that everyone can find something they like.
Industry/Entity Type
Restaurants
Coding
Coded - Design and coding required
Number of Pages Required
5+ page
Font styles to use
Look and feel
Each slider illustrates characteristics of the customer's brand and the style your logo design should communicate.

```html
<!DOCTYPE html>
<html lang="en">
<head>
<meta charset="utf-8">
<title>Tidewell Food Hall</title>
<link href="https://fonts.googleapis.com/css2?family=Playfair+Display:ital,wght@0,400;0,600;0,700;1,400&family=Inter:wght@400;500;600&display=swap" rel="stylesheet">
<style>
:root{
  --navy:#1f4a6b;
  --navy-dark:#223d58;
  --coral:#e8452f;
  --cream:#fbf7f0;
  --blue:#0b57a6;
  --text:#3b4753;
  --muted:#5d6873;
  --line:#e7e9ec;
  --white:#ffffff;
}
*{box-sizing:border-box;margin:0;padding:0}
html,body{width:1200px;height:2576px;overflow:hidden}
body{font-family:'Inter',sans-serif;color:var(--text);background:var(--white);position:relative}
.container{width:844px;margin:0 auto;position:relative}

/* nav */
.site-nav{height:45px;border-bottom:1px solid var(--line);display:flex;align-items:center}
.site-nav .container{display:flex;align-items:center;justify-content:space-between}
.brand{font-family:'Playfair Display',serif;font-weight:600;font-size:16px;color:var(--navy)}
.nav-links{display:flex;gap:30px;font-size:10px;color:var(--navy);margin-right:8px}
.nav-links span{display:flex;align-items:center;gap:5px}

/* hero */
.hero{position:relative;height:390px;overflow:hidden}
.hero-photo{position:absolute;inset:0;background:linear-gradient(110deg,#3c4a44 0%,#6b5a45 30%,#8a6a4a 50%,#4b4e4b 75%,#2f3a3a 100%)}
.hero-shade{position:absolute;inset:0;background:rgba(20,25,30,.35)}
.hero-content{position:relative;text-align:center;color:var(--white);padding-top:118px}
.hero h1{font-family:'Playfair Display',serif;font-weight:600;font-size:40px;line-height:1}
.hero-sub{font-family:'Playfair Display',serif;font-size:15px;line-height:20px;margin-top:14px}
.hero-open{font-family:'Playfair Display',serif;font-style:italic;font-size:15px;margin-top:14px}
.hero-actions{display:flex;justify-content:center;gap:10px;margin-top:18px}
.btn{display:inline-flex;align-items:center;justify-content:center;height:27px;padding:0 20px;font-size:9px;border-radius:2px}
.btn-coral{background:var(--coral);color:var(--white)}
.btn-ghost{border:1px solid var(--white);color:var(--white)}
.hero-wave{position:absolute;left:0;bottom:0;width:1200px;height:70px}

/* section headings */
.section-title{font-family:'Playfair Display',serif;font-weight:600;font-size:23px;color:var(--navy);text-align:center}
.rule{width:50px;height:2px;background:var(--coral);margin:10px auto 0}
.section-lead{font-size:11px;line-height:18px;text-align:center;color:var(--text)}

/* about */
.about{padding-top:68px;height:396px}
.about .section-lead{width:470px;margin:20px auto 0}
.feature-row{display:flex;gap:20px;margin-top:30px}
.feature{flex:1;height:135px;background:var(--white);border-radius:4px;box-shadow:0 1px 4px rgba(0,0,0,.08);padding:14px 15px}
.feature-icon{width:28px;height:28px;border-radius:50%;background:#e4edf5;display:flex;align-items:center;justify-content:center}
.feature h3{font-family:'Playfair Display',serif;font-weight:600;font-size:12px;color:var(--navy);margin-top:12px}
.feature p{font-size:9.5px;line-height:15px;color:var(--muted);margin-top:6px;padding-right:6px}

/* vendors */
.vendors{background:var(--cream);height:893px;padding-top:50px}
.vendors .section-lead{width:460px;margin:17px auto 0}
.filters{display:flex;justify-content:center;gap:5px;margin-top:18px}
.chip{height:24px;padding:0 10px;border:1px solid var(--navy);border-radius:3px;font-size:8.5px;display:flex;align-items:center;color:var(--navy);background:var(--white)}
.chip.active{background:var(--navy);color:var(--white)}
.vendor-grid{display:grid;grid-template-columns:repeat(3,268px);gap:20px 20px;margin-top:50px}
.vendor{height:259px;background:var(--white);border-radius:4px;box-shadow:0 1px 4px rgba(0,0,0,.08);overflow:hidden}
.vendor-photo{height:120px;background:radial-gradient(ellipse at 50% 70%,#2b3550 0%,#4a3a3a 35%,#8a4a2c 70%,#6e3a24 100%)}
.vendor-body{padding:14px 15px}
.tag{display:inline-block;font-size:7px;background:#e4edf5;color:var(--navy);padding:2px 6px;border-radius:8px}
.vendor h3{font-family:'Playfair Display',serif;font-weight:600;font-size:12px;color:var(--navy);margin-top:6px}
.vendor p{font-size:9.5px;line-height:15px;color:var(--muted);margin-top:6px;height:30px}
.btn-blue{background:var(--blue);color:var(--white);height:24px;padding:0 10px;margin-top:10px;font-size:9.5px;border-radius:2px}
.view-all{text-align:center;margin-top:38px;font-family:'Playfair Display',serif;font-size:11px;color:var(--navy);display:flex;justify-content:center;align-items:center;gap:8px}

/* location */
.location{height:349px;position:relative}
.location-text{position:absolute;left:179px;top:60px;width:420px}
.location-text h2{font-family:'Playfair Display',serif;font-weight:600;font-size:22px;color:var(--navy)}
.location-text .rule{margin:9px 0 0}
.location-text p{font-size:10.5px;line-height:18px;margin-top:22px}
.location-text h4{font-family:'Playfair Display',serif;font-weight:600;font-size:12px;color:var(--navy);margin-top:16px}
.address{font-size:9.5px;line-height:17.5px;margin-top:6px}
.hours{font-size:9.5px;margin-top:10px}
.hours b{font-weight:600}
.btn-navy{background:var(--navy);color:var(--white);height:24px;padding:0 10px;margin-top:20px;font-size:8.5px;gap:6px;border-radius:2px}
.map{position:absolute;left:679px;top:7px;width:318px;height:317px;background:linear-gradient(135deg,#e6efe6 0%,#cfeedd 45%,#a9ddea 70%,#8fd3e8 100%)}

/* newsletter */
.newsletter{height:260px;background:linear-gradient(90deg,#214a6a 0%,#2f4c66 55%,#4a5566 100%);color:var(--white);text-align:center;padding-top:52px}
.newsletter h2{font-family:'Playfair Display',serif;font-weight:600;font-size:22px}
.newsletter .rule{margin-top:8px}
.newsletter p{font-size:10.5px;line-height:18px;width:480px;margin:22px auto 0}
.subscribe{display:flex;justify-content:center;gap:10px;margin-top:20px}
.email-field{width:246px;height:25px;border:1px solid rgba(255,255,255,.3);background:rgba(255,255,255,.12);border-radius:2px;font-size:8px;color:rgba(255,255,255,.7);text-align:left;padding:8px 7px}
.btn-sub{height:25px;background:var(--coral);padding:0 10px;font-size:8.5px;border-radius:2px;display:flex;align-items:center}
.privacy{font-size:8px!important;opacity:.8;margin-top:10px!important}

/* footer */
.site-footer{height:243px;background:var(--navy-dark);color:#d6dde5;position:relative}
.footer-cols{display:flex;padding-top:32px}
.footer-col{width:216px}
.footer-col h3{font-family:'Playfair Display',serif;font-weight:600;font-size:14px;color:var(--white)}
.footer-col h4{font-family:'Playfair Display',serif;font-weight:600;font-size:11px;color:var(--white)}
.footer-col p,.footer-col li{font-size:9.5px;line-height:16px;margin-top:4px}
.footer-about p{max-width:185px;margin-top:8px}
.footer-col ul{list-style:none;margin-top:8px}
.footer-col li{line-height:20px;margin-top:0}
.social{display:flex;gap:9px;margin-top:10px}
.social span{width:10px;height:10px;border:1.2px solid #d6dde5;border-radius:50%}
.contact-item{display:flex;align-items:center;gap:6px}
.copyright{position:absolute;bottom:26px;width:100%;text-align:center;font-size:8px;color:#9fb0c0}
</style>
</head>
<body>

<header class="site-nav">
  <div class="container">
    <div class="brand">Tidewell Food Hall</div>
    <nav class="nav-links">
      <span>About</span>
      <span>Vendors
        <svg width="8" height="5" viewBox="0 0 8 5"><path d="M1 1l3 3 3-3" fill="none" stroke="#1f4a6b" stroke-width="1"/></svg>
      </span>
      <span>Location</span>
      <span>Contact</span>
    </nav>
  </div>
</header>

<section class="hero">
  <div class="hero-photo" role="img" aria-label="Food hall counter with fresh dishes and a cook at work"></div>
  <div class="hero-shade"></div>
  <div class="hero-content">
    <h1>Tidewell Food Hall</h1>
    <p class="hero-sub">San Clemente's premier oceanfront culinary destination,<br>featuring 15 local vendors and 2 craft bars</p>
    <p class="hero-open">Opening Summer 2025</p>
    <div class="hero-actions">
      <span class="btn btn-coral">Explore Vendors</span>
      <span class="btn btn-ghost">Get Updates</span>
    </div>
  </div>
  <svg class="hero-wave" viewBox="0 0 1200 70" preserveAspectRatio="none"><path d="M0 40 C250 10 450 5 650 20 C850 35 1000 60 1200 70 L1200 70 L0 70 Z" fill="#fff"/></svg>
</section>

<section class="about">
  <div class="container">
    <h2 class="section-title">A Coastal Culinary Experience</h2>
    <div class="rule"></div>
    <p class="section-lead">Tidewell Food Hall brings together the best of San Clemente's local culinary talent in one stunning oceanfront location. With 15 diverse food vendors and 2 craft bars, we've created a vibrant gathering place for locals and visitors alike.</p>
    <div class="feature-row">
      <div class="feature">
        <div class="feature-icon"><svg width="12" height="12" viewBox="0 0 12 12"><path d="M1 2h4l1 1 1-1h4v8H7l-1 1-1-1H1z M6 3v8" fill="none" stroke="#1f4a6b" stroke-width="1"/></svg></div>
        <h3>Local Flavors</h3>
        <p>Carefully selected vendors that represent the best of San Clemente's culinary scene, from fresh seafood to authentic Mexican cuisine.</p>
      </div>
      <div class="feature">
        <div class="feature-icon"><svg width="12" height="12" viewBox="0 0 12 12"><path d="M1.5 6L6 2l4.5 4V10.5h-3V7.5h-3v3h-3z" fill="none" stroke="#1f4a6b" stroke-width="1"/></svg></div>
        <h3>Oceanfront Setting</h3>
        <p>Located steps from the Pacific Ocean, our beautiful patio offers breathtaking views and the perfect setting for enjoying amazing food.</p>
      </div>
      <div class="feature">
        <div class="feature-icon"><svg width="12" height="12" viewBox="0 0 12 12"><circle cx="4" cy="4" r="1.6" fill="none" stroke="#1f4a6b"/><circle cx="8.5" cy="4.5" r="1.4" fill="none" stroke="#1f4a6b"/><path d="M1 10c0-2 1.5-3 3-3s3 1 3 3M6.5 10c0-1.6 1-2.5 2-2.5s2.5.9 2.5 2.5" fill="none" stroke="#1f4a6b"/></svg></div>
        <h3>Community Hub</h3>
        <p>More than just a place to eat, Tidewell Food Hall is designed to be a gathering place that brings together our coastal community.</p>
      </div>
    </div>
  </div>
</section>

<section class="vendors">
  <div class="container">
    <h2 class="section-title">Our Vendors</h2>
    <div class="rule"></div>
    <p class="section-lead">Discover our collection of 15 carefully selected food vendors and 2 craft bars, each bringing their unique flavors and expertise to Tidewell Food Hall.</p>
    <div class="filters">
      <span class="chip active">All</span><span class="chip">Seafood</span><span class="chip">Mexican</span><span class="chip">Italian</span><span class="chip">American</span><span class="chip">Coffee</span><span class="chip">Bar</span>
    </div>
    <div class="vendor-grid">
      <article class="vendor"><div class="vendor-photo" role="img" aria-label="Berry tart dessert on a wooden table"></div><div class="vendor-body"><span class="tag">Seafood</span><h3>Swellside Poke</h3><p>Fresh, Hawaiian-inspired poke bowls with locally caught fish and organic produce.</p><span class="btn btn-blue">Visit Website</span></div></article>
      <article class="vendor"><div class="vendor-photo" role="img" aria-label="Berry tart dessert on a wooden table"></div><div class="vendor-body"><span class="tag">Mexican</span><h3>Cantera Tacos</h3><p>Authentic Baja-style tacos with sustainable seafood and housemade tortillas.</p><span class="btn btn-blue">Visit Website</span></div></article>
      <article class="vendor"><div class="vendor-photo" role="img" aria-label="Berry tart dessert on a wooden table"></div><div class="vendor-body"><span class="tag">Bar</span><h3>Driftline Bar</h3><p>Craft cocktails and local beers with an emphasis on fresh, seasonal ingredients.</p><span class="btn btn-blue">Visit Website</span></div></article>
      <article class="vendor"><div class="vendor-photo" role="img" aria-label="Berry tart dessert on a wooden table"></div><div class="vendor-body"><span class="tag">Coffee</span><h3>Kelpwood Coffee</h3><p>Small-batch roasted coffee and artisanal pastries made fresh daily.</p><span class="btn btn-blue">Visit Website</span></div></article>
      <article class="vendor"><div class="vendor-photo" role="img" aria-label="Berry tart dessert on a wooden table"></div><div class="vendor-body"><span class="tag">American</span><h3>Lanternfish Grill</h3><p>Classic California cuisine with a focus on flame-grilled specialties.</p><span class="btn btn-blue">Visit Website</span></div></article>
      <article class="vendor"><div class="vendor-photo" role="img" aria-label="Berry tart dessert on a wooden table"></div><div class="vendor-body"><span class="tag">Italian</span><h3>Saltmarsh Pasta</h3><p>Handmade pasta dishes inspired by coastal Italian cuisine.</p><span class="btn btn-blue">Visit Website</span></div></article>
    </div>
    <div class="view-all">View All Vendors <svg width="8" height="5" viewBox="0 0 8 5"><path d="M1 1l3 3 3-3" fill="none" stroke="#1f4a6b"/></svg></div>
  </div>
</section>

<section class="location">
  <div class="location-text">
    <h2>Our Location</h2>
    <div class="rule"></div>
    <p>Located in the heart of San Clemente, Tidewell Food Hall offers breathtaking views of the Pacific Ocean from our expansive outdoor patio.</p>
    <h4>Visit Us</h4>
    <div class="address">480 Harborline Drive<br>San Clemente, CA 92672<br>United States</div>
    <div class="hours"><b>Opening Hours:</b> Coming Summer 2025</div>
    <span class="btn btn-navy">Get Directions
      <svg width="9" height="9" viewBox="0 0 10 10"><circle cx="5" cy="5" r="4" fill="none" stroke="#fff"/><circle cx="5" cy="5" r="1.3" fill="#fff"/></svg>
    </span>
  </div>
  <div class="map" role="img" aria-label="Map of the San Clemente coastline"></div>
</section>

<section class="newsletter">
  <h2>Stay Updated</h2>
  <div class="rule"></div>
  <p>Subscribe to our newsletter to receive the latest updates on our grand opening, featured vendors, special events, and more!</p>
  <div class="subscribe">
    <div class="email-field">Enter your email</div>
    <span class="btn-sub">Subscribe</span>
  </div>
  <p class="privacy">We respect your privacy and will never share your information.</p>
</section>

<footer class="site-footer">
  <div class="container footer-cols">
    <div class="footer-col footer-about">
      <h3>Tidewell Food Hall</h3>
      <p>San Clemente's premier oceanfront culinary destination, opening Summer 2025.</p>
      <div class="social"><span></span><span></span><span></span><span></span></div>
    </div>
    <div class="footer-col">
      <h4>Location</h4>
      <p style="margin-top:8px">480 Harborline Drive<br>San Clemente, CA 92672<br>United States</p>
    </div>
    <div class="footer-col">
      <h4>Quick Links</h4>
      <ul><li>About</li><li>Vendors</li><li>Location</li><li>Careers</li><li>Press</li></ul>
    </div>
    <div class="footer-col">
      <h4>Contact</h4>
      <ul>
        <li class="contact-item"><svg width="9" height="7" viewBox="0 0 9 7"><rect x=".5" y=".5" width="8" height="6" fill="none" stroke="#d6dde5"/><path d="M.5 .5l4 3 4-3" fill="none" stroke="#d6dde5"/></svg>info@tidewellfoodhall.com</li>
        <li class="contact-item"><svg width="9" height="9" viewBox="0 0 9 9"><path d="M3.5 5.5l2-2M2.5 4L1.5 5a1.5 1.5 0 002 2l1-1M6.5 5l1-1a1.5 1.5 0 00-2-2l-1 1" fill="none" stroke="#d6dde5"/></svg>tidewellfoodhall.com</li>
      </ul>
    </div>
  </div>
  <div class="copyright">© 2025 Tidewell Food Hall. All rights reserved.</div>
</footer>

</body>
</html>
```